Design for a 4 screens iOS and Android app - "VelidMetra"

The app allows you to track your car gasoline refill ...
We need a design for the 4 screens of the app:
a) 1 form with 3 fields.
b) 1 simple list view
c) 1 summary view
d) 1 text page
2 "alerts" items are also to be designed.
No specific guidelines, nor logo or whatever.
It will be a free app distributed on iOS and Androïd.
We just want to make it looking nice & very usable for end users.
Target Market(s)
B2C app
Industry/Entity Type
Android

```html
<!DOCTYPE html>
<html lang="en">
<head>
<meta charset="utf-8">
<title>VelidMetra – Add refill</title>
<link href="https://fonts.googleapis.com/css2?family=Roboto:wght@500;900&display=swap" rel="stylesheet">
<style>
  :root {
    --bar-blue: #0088ff;
    --sky-top: #7bbfe8;
    --sky-bottom: #2569b8;
    --field-bg: #ffffff;
    --placeholder: #a6a6a6;
    --white: #ffffff;
  }
  * { margin: 0; padding: 0; box-sizing: border-box; }
  html, body { width: 675px; height: 1200px; overflow: hidden; }
  body {
    font-family: "Roboto", Arial, sans-serif;
    background: linear-gradient(to bottom, var(--sky-top) 0%, var(--sky-top) 60%, var(--sky-bottom) 100%);
    position: relative;
  }
  .tab-bar {
    position: absolute; top: 0; left: 0; width: 675px; height: 107px;
    display: flex; background: var(--bar-blue);
  }
  .tab {
    flex: 1; display: flex; align-items: center; justify-content: center;
  }
  .tab + .tab { border-left: 1px solid var(--white); }
  .tab svg { display: block; }
  .refill-form { position: absolute; left: 0; top: 0; width: 675px; }
  .field {
    position: absolute; height: 80px; border-radius: 22px;
    background: var(--field-bg);
    display: flex; align-items: center; padding-left: 50px;
    font-weight: 500; font-size: 32px; color: var(--placeholder);
    letter-spacing: 0.3px;
  }
  .field-odometer { left: 86px; width: 504px; top: 364px; }
  .field-litres { left: 88px; width: 500px; top: 483px; }
  .field-price { left: 88px; width: 500px; top: 597px; }
  .save-button {
    position: absolute; left: 197px; top: 791px; width: 282px; height: 85px;
    border-radius: 20px; background: var(--bar-blue);
    display: flex; align-items: center; justify-content: center;
    color: var(--white); font-weight: 900; font-size: 35px;
  }
  .about-link {
    position: absolute; left: 0; width: 675px; top: 1064px;
    text-align: center; color: var(--white); font-weight: 500; font-size: 27px;
  }
</style>
</head>
<body>
  <nav class="tab-bar">
    <div class="tab" aria-label="Add refill">
      <svg width="46" height="46" viewBox="0 0 46 46">
        <path d="M23 1v44M1 23h44" stroke="#fff" stroke-width="3.5" stroke-linecap="round"/>
      </svg>
    </div>
    <div class="tab" aria-label="Refill list">
      <svg width="62" height="44" viewBox="0 0 62 44">
        <g fill="#fff"><circle cx="4.5" cy="4" r="4"/><circle cx="4.5" cy="22" r="4"/><circle cx="4.5" cy="40" r="4"/></g>
        <g stroke="#fff" stroke-width="3.5" stroke-linecap="round"><path d="M19 4h41M19 22h41M19 40h41"/></g>
      </svg>
    </div>
    <div class="tab" aria-label="Summary">
      <svg width="58" height="46" viewBox="0 0 58 46">
        <path d="M2 2v42h54" fill="none" stroke="#fff" stroke-width="3.5" stroke-linecap="round" stroke-linejoin="round"/>
        <path d="M9 36v-12l6-6 6 5 8-10 8 8 13 15z" fill="#fff" stroke="#fff" stroke-width="2" stroke-linejoin="round"/>
      </svg>
    </div>
  </nav>

  <main class="refill-form">
    <div class="field field-odometer">127500</div>
    <div class="field field-litres">LITRES</div>
    <div class="field field-price">PRICE</div>
    <div class="save-button">Save</div>
  </main>

  <div class="about-link">About us</div>
</body>
</html>
```